Newspaper Ad for Cool Hawaiian PPE Company

We need an incredible ad for our local newspaper to tell everyone about BreezeGuard.com. We want a beautiful ad that is sophisticated with a local flair. Less is more. Clean. Stands out. We are safely shipping masks and PPE to our local community. Everyone has access to the supplies they need to keep them and their loved ones safe during the pandemic. Make it really pop.

Target Market(s)

Community members

Requirements
Must have
• Half Page:

Specs 9.7” x 10” column inches for the half page. Minimum 300 dpi, jpeg is fine.

```html
<!DOCTYPE html>
<html lang="en">
<head>
<meta charset="utf-8">
<title>BreezeGuard.com Half Page Ad</title>
<link href="https://fonts.googleapis.com/css2?family=Montserrat:wght@300;400;600;700;800&family=Varela+Round&display=swap" rel="stylesheet">
<style>
  :root {
    --green: #148a3e;
    --green-deep: #127a37;
    --grey-text: #666666;
    --grey-dark: #5a5a5a;
    --white: #ffffff;
    --icon: #555555;
    --room: #f2f1ee;
    --leaf: #4f7a3a;
    --denim: #8fb3d4;
    --rust: #a0552a;
    --wine: #8a2a30;
    --carton: #c9a77c;
  }
  * { margin: 0; padding: 0; box-sizing: border-box; }
  html, body { width: 1170px; height: 1200px; overflow: hidden; background: var(--white); }
  .ad {
    position: relative;
    width: 1170px; height: 1200px;
    background: var(--white);
    font-family: "Montserrat", sans-serif;
    overflow: hidden;
  }
  .photo {
    position: absolute; left: 0; top: 166px; width: 1170px; height: 720px;
    background:
      radial-gradient(ellipse 240px 300px at 1080px 380px, rgba(79,122,58,0.55), rgba(79,122,58,0) 100%),
      radial-gradient(ellipse 170px 260px at 60px 480px, rgba(79,122,58,0.45), rgba(79,122,58,0) 100%),
      radial-gradient(ellipse 200px 180px at 130px 560px, rgba(201,167,124,0.55), rgba(201,167,124,0) 100%),
      radial-gradient(ellipse 220px 160px at 870px 500px, rgba(201,167,124,0.5), rgba(201,167,124,0) 100%),
      radial-gradient(ellipse 200px 260px at 370px 470px, rgba(143,179,212,0.55), rgba(143,179,212,0) 100%),
      radial-gradient(ellipse 170px 200px at 730px 530px, rgba(143,179,212,0.6), rgba(143,179,212,0) 100%),
      radial-gradient(ellipse 180px 230px at 580px 420px, rgba(255,255,255,0.9), rgba(255,255,255,0) 100%),
      radial-gradient(ellipse 220px 120px at 430px 650px, rgba(160,85,42,0.55), rgba(160,85,42,0) 100%),
      radial-gradient(ellipse 200px 120px at 880px 620px, rgba(138,42,48,0.45), rgba(138,42,48,0) 100%),
      radial-gradient(ellipse 260px 110px at 800px 700px, rgba(110,110,110,0.35), rgba(110,110,110,0) 100%),
      linear-gradient(180deg, #f4f4f2 0%, #efeeeb 40%, #e4dfd8 80%, #d8d1c7 100%);
  }
  .url-tab { position: absolute; left: 892px; top: 0; width: 225px; height: 76px; }
  .url-tab svg { position: absolute; inset: 0; }
  .url-tab span {
    position: absolute; left: 0; right: 0; top: 30px;
    text-align: center; color: var(--white);
    font-weight: 700; font-size: 16px;
  }
  .headline {
    position: absolute; left: 0; right: 0; top: 126px;
    text-align: center; color: var(--grey-text);
    font-size: 47px; line-height: 59px; letter-spacing: -0.5px;
  }
  .headline .light { font-weight: 300; }
  .headline .strong-green { font-weight: 800; color: var(--green); }
  .headline .strong-grey { font-weight: 800; color: var(--grey-dark); }
  .band {
    position: absolute; left: 0; top: 870px; width: 1170px; height: 159px;
    background: linear-gradient(180deg, var(--green) 0%, var(--green-deep) 100%);
  }
  .products { position: absolute; left: 0; top: 0; width: 1170px; height: 1029px; }
  .product { position: absolute; width: 200px; margin-left: -100px; top: 794px; text-align: center; }
  .product .badge {
    width: 134px; height: 134px; margin: 0 auto;
    border-radius: 50%; background: var(--white);
    border: 4px solid var(--green);
    display: flex; align-items: center; justify-content: center;
    box-shadow: 0 3px 6px rgba(0,0,0,0.15);
  }
  .product .badge svg { width: 96px; height: 96px; }
  .product .label {
    margin-top: 12px; color: var(--white);
    font-family: "Varela Round", sans-serif; font-size: 28px; white-space: nowrap;
    -webkit-text-stroke: 0.6px var(--white);
  }
  .perks {
    position: absolute; left: 55px; top: 1076px;
    display: flex; gap: 28px;
    color: var(--grey-text); font-weight: 600; font-size: 25px; letter-spacing: 0.3px;
  }
  .perk { display: flex; align-items: center; gap: 10px; }
  .perk svg { width: 22px; height: 22px; }
  .tagline {
    position: absolute; left: 60px; top: 1120px;
    color: var(--green); font-weight: 800; font-size: 42px; letter-spacing: 0.5px;
  }
  .brand {
    position: absolute; right: 52px; top: 1088px;
    display: flex; align-items: center; gap: 12px;
  }
  .brand .dot { width: 26px; height: 26px; border-radius: 50%; background: var(--green); }
  .brand .name { color: var(--grey-dark); font-weight: 700; font-size: 44px; letter-spacing: -1px; }
  .brand-rule {
    position: absolute; right: 52px; top: 1150px; width: 330px; height: 3px;
    background: var(--green);
  }
</style>
</head>
<body>
<div class="ad">
  <div class="photo" role="img" aria-label="Family of three in face masks sitting on the floor of a bright room with moving boxes and potted plants"></div>

  <div class="url-tab">
    <svg viewBox="0 0 225 76" width="225" height="76" aria-hidden="true">
      <path d="M0 0 H225 V76 L112 62 L0 76 Z" fill="var(--green)"/>
      <path d="M0 76 L112 62 L225 76" fill="none" stroke="#6b6b6b" stroke-width="3"/>
    </svg>
    <span>www.breezeguard.com</span>
  </div>

  <h1 class="headline">
    <span class="light">PERSONAL </span><span class="strong-green">PROTECTIVE EQUIPMENT</span><br>
    <span class="light">FOR </span><span class="strong-grey">FAMILY &amp; BUSINESS</span>
  </h1>

  <div class="band"></div>

  <div class="products">
    <div class="product" style="left:140px">
      <div class="badge">
        <svg viewBox="0 0 96 96" fill="none" stroke="var(--icon)" stroke-width="3.5" stroke-linecap="round" stroke-linejoin="round">
          <path d="M22 34 Q48 26 74 34 V60 Q48 70 22 60 Z"/>
          <path d="M22 38 Q8 36 8 48 Q8 60 22 58"/>
          <path d="M74 38 Q88 36 88 48 Q88 60 74 58"/>
          <path d="M26 44 Q48 38 70 44"/>
          <path d="M26 52 Q48 48 70 52"/>
        </svg>
      </div>
      <div class="label">Masks</div>
    </div>
    <div class="product" style="left:358px">
      <div class="badge">
        <svg viewBox="0 0 96 96" fill="none" stroke="var(--icon)" stroke-width="3" stroke-linecap="round" stroke-linejoin="round">
          <rect x="32" y="8" width="32" height="26" rx="3"/>
          <path d="M44 21 H52 M48 17 V25"/>
          <path d="M46 34 V40 H50 V34"/>
          <path d="M48 44 Q44 50 48 54 Q52 50 48 44 Z"/>
          <path d="M10 78 L26 66 Q34 62 44 66 H58 Q62 68 58 72 H44"/>
          <path d="M58 72 L78 62 Q84 60 84 66 L62 82 Q56 86 46 86 H20"/>
        </svg>
      </div>
      <div class="label">Hand Sanitizer</div>
    </div>
    <div class="product" style="left:574px">
      <div class="badge">
        <svg viewBox="0 0 96 96" fill="none" stroke="var(--icon)" stroke-width="3" stroke-linecap="round" stroke-linejoin="round">
          <path d="M30 30 Q30 12 52 12 Q74 12 74 34 V52 Q74 60 68 64 L72 84"/>
          <path d="M22 34 H80"/>
          <path d="M24 34 V78 L44 82"/>
          <path d="M36 40 Q34 50 40 56 L36 62 L42 66 L40 74"/>
        </svg>
      </div>
      <div class="label">Face Shields</div>
    </div>
    <div class="product" style="left:791px">
      <div class="badge">
        <svg viewBox="0 0 96 96" fill="none" stroke="var(--icon)" stroke-width="3" stroke-linecap="round" stroke-linejoin="round">
          <path d="M22 18 H56 V28 H22 Q18 24 22 18 Z"/>
          <path d="M30 28 L26 40 Q22 46 22 54 V86 H56 V52 Q56 44 48 40 V28"/>
          <rect x="32" y="58" width="14" height="14" rx="2"/>
          <path d="M39 61 V69 M35 65 H43"/>
          <path d="M62 20 H68 M72 14 L76 12 M72 24 L76 26"/>
          <circle cx="84" cy="20" r="3"/>
        </svg>
      </div>
      <div class="label">Disinfectant</div>
    </div>
    <div class="product" style="left:1008px">
      <div class="badge">
        <svg viewBox="0 0 96 96" fill="none" stroke="var(--icon)" stroke-width="3" stroke-linecap="round" stroke-linejoin="round">
          <path d="M18 44 Q14 30 20 28 Q24 28 26 36 L30 20 Q34 16 36 22 L38 16 Q42 12 44 18 L46 40 Q50 50 46 62 L44 74 L26 76 Q20 60 18 44 Z"/>
          <path d="M26 76 L28 84 L46 82 L44 74"/>
          <path d="M54 22 Q58 14 62 22 L64 16 Q68 12 70 18 L74 14 Q78 12 78 20 L76 40 Q82 36 86 42 L72 64 L74 74 L56 78 Q50 60 52 40 Z"/>
          <path d="M56 78 L58 86 L76 82 L74 74"/>
        </svg>
      </div>
      <div class="label">Gloves</div>
    </div>
  </div>

  <div class="perks">
    <div class="perk">
      <svg viewBox="0 0 22 22" aria-hidden="true"><circle cx="11" cy="11" r="11" fill="var(--green)"/><path d="M6 11.5 L9.5 15 L16 7.5" fill="none" stroke="#fff" stroke-width="2.6" stroke-linecap="round" stroke-linejoin="round"/></svg>
      <span>FREE SHIPPING</span>
    </div>
    <div class="perk">
      <svg viewBox="0 0 22 22" aria-hidden="true"><circle cx="11" cy="11" r="11" fill="var(--green)"/><path d="M6 11.5 L9.5 15 L16 7.5" fill="none" stroke="#fff" stroke-width="2.6" stroke-linecap="round" stroke-linejoin="round"/></svg>
      <span>LOCALLY STOCKED</span>
    </div>
  </div>

  <p class="tagline">WE’VE GOT YOU HAWAII!!</p>

  <div class="brand">
    <span class="dot" aria-hidden="true"></span>
    <span class="name">BreezeGuard.com</span>
  </div>
  <div class="brand-rule" aria-hidden="true"></div>
</div>
</body>
</html>
```